Professional & Modern Technology Business Card

We need a business card for our software/technology firm. Our services include Program/Project Management, Project Controls and Enterprise Analytics. Our clients are usually in the Aviation, Public Works, Transportation and Electric & Water Utility industries. We serve both public and private clients. Would like a very professional, conservative but somewhat modern design. Design, Develop, Deploy is the corporate tagline. We have two offices. The headquarters is in Atlanta, GA and a satellite office In Savannah, GA. Corporate Logo Attached.
Looking to do website and corporate brochure after the successful completion of this project. Would like to begin a working relationship with best designers.
Tagline: Design, Develop, Deploy
Website: www.quelvanesystems.example
My Name: Marla Dunstead
My Title: CEO
Email: mdunstead@quelvanesystems.example
Atlanta Address:
87 Corliss Avenue, #2291
Atlanta, GA 30301
Office: 404.555.0182
Fax: 404.555.0147
Mobile: 404.555.0163
Savannah Address:
350 West Harrow Bend Road
Suite 720
Savannah, GA 31401
Office: 912.555.0139
Fax: 404.555.0147
Mobile: 404.555.0163
Updates
Please include the email address in your designs: mdunstead@quelvanesystems.example.
I appreciate everyone's design efforts. Just a few notes:
1. Please remove the mobile number from the cards
2. The backs of the cards can be utilized for writing notes. Make sure your design on the back of the card is conducive to clearly adding writing if needed.
3. No black backgrounds please
4. Only use the corporate logo on the front of the card. You can use portions of the logo design, but not the logo in totality.
Thank You
Industry/Entity Type
Conservative
Look and feel
Each slider illustrates characteristics of the customer's brand and the style your logo design should communicate.

```html
<!DOCTYPE html>
<html lang="en">
<head>
<meta charset="utf-8">
<title>Quelvane Systems, Inc. — Business Card</title>
<link rel="stylesheet" href="https://fonts.googleapis.com/css2?family=Oswald:wght@300;400;600&display=swap">
<style>
  :root {
    --backdrop: #d6d6d6;
    --card-white: #f4f4f4;
    --brand-green: #8dc63f;
    --brand-green-dark: #7ab32e;
    --band-grey: #a9a9a9;
    --rule-faint: #dcdcdc;
    --ink: #3a3a3a;
    --ink-soft: #6b6b6b;
    --white: #ffffff;
  }
  * { box-sizing: border-box; margin: 0; padding: 0; }
  html, body {
    width: 1200px; height: 511px; overflow: hidden;
    background: var(--backdrop);
    font-family: "Oswald", "Arial Narrow", sans-serif;
    color: var(--ink);
  }
  .sheet { position: relative; width: 1200px; height: 511px; }
  .card {
    position: absolute; top: 101px; width: 540px; height: 309px;
    overflow: hidden; background: var(--card-white);
  }
  .card--back { left: 40px; background: var(--white); }
  .card--front { left: 620px; }

  /* back side: light writing area between two green bands */
  .back-band {
    position: absolute; left: 0; right: 0; background: var(--brand-green);
  }
  .back-band--top { top: 0; height: 44px; }
  .back-band--bottom { bottom: 0; height: 56px; }
  .back-tagline {
    position: absolute; left: 0; right: 0; top: 12px;
    text-align: center; color: var(--white);
    font-weight: 400; font-size: 13px; letter-spacing: 5px;
  }
  .back-website {
    position: absolute; left: 0; right: 0; bottom: 20px;
    text-align: center; color: var(--white);
    font-weight: 400; font-size: 13px; letter-spacing: 6px;
  }
  .note-lines {
    position: absolute; left: 40px; right: 40px; top: 78px;
    list-style: none;
  }
  .note-lines li {
    height: 34px; border-bottom: 1px solid var(--rule-faint);
  }

  /* wordmark */
  .wordmark { display: flex; align-items: center; gap: 9px; }
  .wordmark__dot {
    width: 18px; height: 18px; border-radius: 50%;
    background: var(--brand-green); flex: none;
  }
  .wordmark__name {
    font-weight: 400; color: var(--ink); line-height: 1.05; font-size: 26px;
  }

  /* front side */
  .front-logo { position: absolute; left: 190px; top: 26px; }
  .person { position: absolute; left: 26px; top: 96px; }
  .person__name { font-weight: 600; font-size: 25px; line-height: 1.1; color: var(--ink); }
  .person__title { font-weight: 300; font-size: 11px; color: var(--ink-soft); }
  .email {
    position: absolute; right: 24px; top: 114px;
    display: flex; align-items: center; gap: 7px;
    font-weight: 300; font-size: 13px; color: var(--ink-soft);
  }
  .divider { position: absolute; left: 0; top: 146px; width: 540px; height: 12px; }

  .office { position: absolute; top: 168px; width: 240px; }
  .office--atlanta { left: 26px; }
  .office--savannah { right: 24px; text-align: right; }
  .office__heading {
    font-weight: 600; font-size: 12.5px; color: var(--ink);
    padding-bottom: 4px; border-bottom: 1px solid var(--brand-green);
    margin-bottom: 6px;
  }
  .office__address { font-weight: 300; font-size: 10.5px; color: var(--ink-soft); margin-bottom: 8px; }
  .phones { list-style: none; }
  .phones li {
    display: flex; align-items: center; gap: 7px;
    font-weight: 300; font-size: 11px; color: var(--ink-soft);
    height: 17px;
  }
  .office--savannah .phones li { justify-content: flex-end; }
  .icon { width: 13px; height: 13px; flex: none; }
</style>
</head>
<body>
<main class="sheet">

  <section class="card card--back" aria-label="Card back">
    <div class="back-band back-band--top">
      <p class="back-tagline">DESIGN, DEVELOP, DEPLOY</p>
    </div>
    <ul class="note-lines" aria-hidden="true">
      <li></li><li></li><li></li><li></li><li></li>
    </ul>
    <div class="back-band back-band--bottom">
      <p class="back-website">WWW.QUELVANESYSTEMS.EXAMPLE</p>
    </div>
  </section>

  <section class="card card--front" aria-label="Card front">
    <div class="front-logo wordmark">
      <span class="wordmark__dot"></span>
      <span class="wordmark__name">Quelvane<br>Systems, Inc.</span>
    </div>

    <div class="person">
      <h1 class="person__name">Marla Dunstead</h1>
      <p class="person__title">CEO</p>
    </div>

    <p class="email">
      <svg class="icon" viewBox="0 0 16 16" aria-hidden="true">
        <rect x="1" y="3" width="14" height="10" rx="1.5" fill="var(--brand-green)"/>
        <path d="M2 4.5 L8 9 L14 4.5" fill="none" stroke="var(--white)" stroke-width="1.3"/>
      </svg>
      mdunstead@quelvanesystems.example
    </p>

    <svg class="divider" viewBox="0 0 540 12" aria-hidden="true">
      <polygon points="0,0 168,0 178,12 0,12" fill="var(--brand-green)"/>
      <polygon points="174,0 540,0 540,12 184,12" fill="var(--band-grey)"/>
    </svg>

    <div class="office office--atlanta">
      <h2 class="office__heading">Atlanta Address</h2>
      <p class="office__address">87 Corliss Avenue, #2291, Atlanta, GA 30301</p>
      <ul class="phones">
        <li>
          <svg class="icon" viewBox="0 0 16 16" aria-hidden="true"><path d="M2 6 Q8 1 14 6 L12 8 L10 6.5 L6 6.5 L4 8 Z" fill="var(--brand-green)"/><rect x="4" y="9" width="8" height="5" rx="1" fill="var(--brand-green)"/></svg>
          404.555.0182
        </li>
        <li>
          <svg class="icon" viewBox="0 0 16 16" aria-hidden="true"><rect x="4" y="1" width="8" height="5" fill="var(--brand-green)"/><rect x="1" y="6" width="14" height="7" rx="1" fill="var(--brand-green)"/><rect x="4" y="11" width="8" height="4" fill="var(--brand-green-dark)"/></svg>
          404.555.0147
        </li>
      </ul>
    </div>

    <div class="office office--savannah">
      <h2 class="office__heading">Savannah Address</h2>
      <p class="office__address">350 West Harrow Bend Road, Suite 720, Savannah, GA 31401</p>
      <ul class="phones">
        <li>
          912.555.0139
          <svg class="icon" viewBox="0 0 16 16" aria-hidden="true"><path d="M2 6 Q8 1 14 6 L12 8 L10 6.5 L6 6.5 L4 8 Z" fill="var(--brand-green)"/><rect x="4" y="9" width="8" height="5" rx="1" fill="var(--brand-green)"/></svg>
        </li>
        <li>
          404.555.0147
          <svg class="icon" viewBox="0 0 16 16" aria-hidden="true"><rect x="4" y="1" width="8" height="5" fill="var(--brand-green)"/><rect x="1" y="6" width="14" height="7" rx="1" fill="var(--brand-green)"/><rect x="4" y="11" width="8" height="4" fill="var(--brand-green-dark)"/></svg>
        </li>
      </ul>
    </div>
  </section>

</main>
</body>
</html>
```